Meridale Networks, it support and management

We run an IT business, so techy style would work well. We need a re-design, now that we’ve moved and phone numbers have changed.

On the back of the card I like having something that helps with taking notes, like a grid or lines

The attachment is the current business card I am using.

We specialize in helping out in all kinds of support, including laptops, desktops, servers, and providing software solutions, like vexora 880, backups and ransomware prevention

Target Market(s)

Other small business owners, specifically smaller than 50 employees

Industry/Entity Type

SMB, but no specific niche

Contact Information for Business Card

I’d like the logo, name, my title/rolw, my contact details

Colors
0094D4
00A9DD
6FCCEA
C7EBF8
E9F6FB

Requirements
Must have
• The ability to take notes on the back of the card
Nice to have
• A new slogan or fun little quip, but not necessary
Should not have
• Street address of any kind.

```html
<!DOCTYPE html>
<html lang="en">
<head>
<meta charset="utf-8">
<title>Meridale Networks – Business Card</title>
<link rel="stylesheet" href="https://fonts.googleapis.com/css2?family=Inter:wght@400;600;700&display=swap">
<style>
  :root {
    --backdrop: #959595;
    --card-white: #ffffff;
    --brand-blue: #4286f5;
    --brand-blue-deep: #3a73d4;
    --note-line: rgba(255, 255, 255, 0.35);
    --ink: #111111;
    --muted: #6d6d6d;
    --dot-field: #f7f7f7;
  }
  * { box-sizing: border-box; margin: 0; padding: 0; }
  html, body {
    width: 1200px; height: 1200px; overflow: hidden;
    background: var(--backdrop);
    font-family: "Inter", Arial, sans-serif;
  }
  .canvas { position: relative; width: 1200px; height: 1200px; }
  .card {
    position: absolute; left: 226px; width: 747px; height: 435px;
    border-radius: 25px; overflow: hidden;
  }
  .card-front { top: 115px; background: var(--card-white); }
  .card-back { top: 626px; background: var(--brand-blue); }

  .dot-field {
    position: absolute; left: 22px; top: 16px; width: 366px; height: 403px;
    background: var(--dot-field);
  }
  .brand {
    position: absolute; right: 52px; top: 58px;
    display: flex; align-items: center; gap: 12px;
    font-size: 26px; font-weight: 700; color: var(--brand-blue);
    letter-spacing: -0.2px;
  }
  .brand-dot {
    width: 22px; height: 22px; border-radius: 50%; background: var(--brand-blue);
  }
  .contact {
    position: absolute; right: 52px; top: 206px; text-align: right;
    line-height: 1.2;
  }
  .contact-name { font-size: 21px; font-weight: 700; color: var(--ink); }
  .contact-role { font-size: 21px; font-weight: 700; color: var(--brand-blue); }
  .contact-lines { margin-top: 16px; font-size: 21px; color: var(--muted); line-height: 1.2; }
  .contact-web { margin-top: 26px; font-size: 21px; color: var(--muted); }
  .contact-web strong { color: var(--brand-blue); font-weight: 700; }

  .note-lines {
    position: absolute; left: 48px; right: 48px;
    background: repeating-linear-gradient(
      to bottom,
      transparent 0, transparent 35px,
      var(--note-line) 35px, var(--note-line) 36px
    );
  }
  .note-lines-top { top: 20px; height: 144px; }
  .note-lines-bottom { top: 272px; height: 144px; }

  .back-brand {
    position: absolute; left: 0; right: 0; top: 168px; height: 100px;
    display: flex; align-items: center; justify-content: center; gap: 16px;
    font-size: 44px; font-weight: 700; color: var(--brand-blue-deep);
  }
  .back-brand .brand-dot { width: 40px; height: 40px; background: var(--brand-blue-deep); }
</style>
</head>
<body>
<main class="canvas">
  <section class="card card-front">
    <div class="dot-field" role="img" aria-label="Faint grey dot grid pattern"></div>
    <div class="brand"><span class="brand-dot"></span>Meridale Networks</div>
    <div class="contact">
      <p class="contact-name">Dana Keller</p>
      <p class="contact-role">President</p>
      <div class="contact-lines">
        <p>danak@meridalenet.com</p>
        <p>555.014.2290</p>
      </div>
      <p class="contact-web"><strong>meridalenet</strong>.com</p>
    </div>
  </section>

  <section class="card card-back">
    <div class="note-lines note-lines-top"></div>
    <div class="back-brand"><span class="brand-dot"></span>Meridale Networks</div>
    <div class="note-lines note-lines-bottom"></div>
  </section>
</main>
</body>
</html>
```